Pell Hartwick - Magazine

Our client would like a magazine designed for a conceptual novelty based on unconventional views on contemporary issues, including; finance, religion, politics etc.!

The novelty includes 1 main article, supporting images and 12 short poems.
We would like the designer to create page vectors, borders, fonts and other layout design elements.

In the first stage of the competition we request:

Magazine layout - 6 pages( 4 article variations based on article content and 2 poem page designs)

We would like to see high impact, striking vectors and design concepts to compliment the article content. See attached bullet point guide to article to help design page themes.

COMPANY INFO
Writer, poet, researcher and commentator. Our client is interested in sharing art and issues he believes in. Our client would like to design one magazine issue first but has a collection of material to produce a series of magazines in the future. So he is looking to establish a potentially long-term partnership with designer(s).

Target Market(s)

Quick and easy to read, coffee time magazine. Target Market: Male 40yrs+, Intellectual, Open Minded.

Industry/Entity Type

Finance

Font styles to use
Serif
Decorative

Requirements
Must have
• Main Article and Poetry: Space for 1 -2 images per page.
A subtle design feature that connects each page.
Primary colors: Jade Green and some Grayscale.
Secondary Colors: 3rd and 4th color open to designers preference.
Page Dimensions : 7.5in height, 7in width.
Articles: Same color theme, different layout and vector choice, same font color and size.
Poetry: Some design creative freedom. Focus on creating a unique title font incorporating the theme of the poem, Poetry TITLE font must be made a feature design element (poem identity)
Font: See Veldtrove Quarterly magazine styling
Columns: Single or multiple.
All vectors and images should be sourced from pixel quarry.
Nice to have
• Images/pictures that connect with article topic and align with color theme.
Should not have
• Avoid repetition of page design. To do this follow the idea of each paragraph (see attached breakdown)

```html
<!DOCTYPE html>
<html lang="en">
<head>
<meta charset="utf-8">
<title>Doctors Destroy Health – Magazine Spread</title>
<link href="https://fonts.googleapis.com/css2?family=Titillium+Web:wght@400;600;700&display=swap" rel="stylesheet">
<style>
  :root {
    --jade: #4a8b6f;
    --jade-deep: #2f6e55;
    --ink: #3a3a3a;
    --ink-soft: #666;
    --paper: #ffffff;
    --stage: #e8e8e8;
    --rule: #d6d6d6;
  }
  * { box-sizing: border-box; margin: 0; padding: 0; }
  html, body { width: 1200px; height: 800px; overflow: hidden; }
  body { background: var(--stage); font-family: "Titillium Web", Arial, sans-serif; color: var(--ink); }

  .spread {
    position: absolute; left: 40px; top: 100px;
    width: 1120px; height: 600px; display: flex;
    box-shadow: 0 6px 24px rgba(0,0,0,.18);
  }
  .page { position: relative; width: 560px; height: 600px; background: var(--paper); overflow: hidden; }
  .page--left::after, .page--right::before {
    content: ""; position: absolute; top: 0; bottom: 0; width: 28px; pointer-events: none;
  }
  .page--left::after { right: 0; background: linear-gradient(to right, rgba(0,0,0,0), rgba(0,0,0,.10)); }
  .page--right::before { left: 0; background: linear-gradient(to left, rgba(0,0,0,0), rgba(0,0,0,.10)); z-index: 3; }

  .photo { position: absolute; }
  .photo--surgery-a { left: 60px; top: 0; width: 208px; height: 140px; background: linear-gradient(150deg, #a9c7cc, #4d7c86); }
  .photo--surgery-b { left: 60px; top: 146px; width: 208px; height: 164px; background: linear-gradient(160deg, #9fc3c8, #3f7280); }
  .photo--surgery-c { left: 274px; top: 0; width: 286px; height: 310px; background: linear-gradient(170deg, #c8d9dc, #5f8c94 55%, #3c6770); }

  .story-title {
    position: absolute; left: 64px; top: 322px;
    font-size: 27px; font-weight: 700; color: var(--jade-deep); letter-spacing: .3px; line-height: 1;
  }
  .story-title::before {
    content: ""; position: absolute; left: -20px; top: -4px; width: 10px; height: 40px; background: var(--jade);
  }
  .story-deck {
    position: absolute; left: 64px; top: 354px; width: 440px;
    font-size: 10.5px; line-height: 13px; color: var(--jade);
  }
  .story-body {
    position: absolute; left: 64px; top: 392px; width: 450px; height: 168px;
    column-count: 3; column-gap: 16px;
    font-size: 7.6px; line-height: 9.8px; color: var(--ink); text-align: justify; overflow: hidden;
  }
  .story-body p + p { margin-top: 6px; }
  .dropcap { float: left; font-size: 30px; line-height: 24px; margin: 1px 3px 0 0; font-weight: 600; color: var(--ink); }

  .folio { position: absolute; bottom: 12px; display: flex; align-items: center; gap: 6px; font-size: 9px; color: var(--ink-soft); }
  .folio__num { width: 20px; height: 20px; background: var(--jade); color: #fff; font-size: 10px; display: flex; align-items: center; justify-content: center; }
  .folio__mag { color: var(--jade); }
  .folio--left { left: 30px; }
  .folio--right { right: 30px; }

  .feature-title {
    position: absolute; left: 40px; top: 16px; width: 460px;
    font-size: 25px; font-weight: 600; line-height: 24px; color: var(--jade-deep);
  }
  .feature-deck { position: absolute; left: 40px; top: 70px; width: 470px; font-size: 10.5px; line-height: 12px; color: var(--jade); }

  .callout {
    position: absolute; left: 0; top: 118px; width: 236px; height: 134px;
    background: var(--jade); color: #fff; padding: 12px 26px 10px 18px;
    font-size: 8px; line-height: 10.5px; text-align: justify; overflow: hidden;
    clip-path: polygon(0 0, 94% 0, 94% 12%, 100% 18%, 94% 24%, 94% 100%, 0 100%);
  }

  .photo--scales { left: 240px; top: 118px; width: 128px; height: 146px; background: linear-gradient(160deg, #d9c79a, #9a6f3a 55%, #6b4a2a); }
  .photo--money { left: 0; top: 272px; width: 208px; height: 128px; background: linear-gradient(140deg, #e6dcc6, #c49a6a 55%, #e0812f);
    clip-path: polygon(0 0, 94% 0, 94% 8%, 100% 14%, 94% 20%, 94% 100%, 0 100%); }
  .photo--head { left: 218px; top: 352px; width: 122px; height: 148px; background: linear-gradient(170deg, #6e9aa3, #40636b 60%, #9fb9a4); }
  .photo--blister { left: 0; top: 408px; width: 208px; height: 154px; background: linear-gradient(135deg, #e8dfe6, #c9879b 45%, #8fa5c8); }

  .brief { position: absolute; font-size: 7.4px; line-height: 9.4px; color: var(--ink); overflow: hidden; }
  .brief__head { font-size: 8.5px; font-weight: 600; color: var(--ink); letter-spacing: .2px; margin-bottom: 2px; }
  .brief--scales { left: 378px; top: 118px; width: 156px; height: 150px; }
  .brief--money { left: 218px; top: 274px; width: 316px; height: 74px; }
  .brief--head { left: 350px; top: 354px; width: 184px; height: 146px; }
  .brief--bottom { left: 218px; top: 506px; width: 316px; height: 60px; }
</style>
</head>
<body>
<main class="spread">
  <section class="page page--left">
    <div class="photo photo--surgery-a" role="img" aria-label="Photograph of surgeons in scrubs working under operating lights"></div>
    <div class="photo photo--surgery-b" role="img" aria-label="Photograph of masked surgical team looking down at the patient"></div>
    <div class="photo photo--surgery-c" role="img" aria-label="Photograph of an operating theatre with surgeons around the table"></div>

    <h1 class="story-title">DOCTORS DESTROY HEALTH</h1>
    <p class="story-deck">Deals with the pharmaceutical industry. perionem vendios alitiorunt ha Ego coniu viverrit, con Ita Ro id moOc, essis. Habentust nos, condes recto Catum quemqueEbus critiu</p>

    <div class="story-body">
      <p><span class="dropcap">M</span>us eos simenia qui nullup taes doluptas doluptasin possusa ntione re, qui ut eicae sapit vita volla quam apidit repudan iscitstrum fero blabore pudiam rem auda velicipid es explabo. At aliquatemque estessitae corempories et des alliborem ut moluptatqui alit et eatis que num sita nonsendis suntur sit, sendign iscimus.</p>
      <p>Odist in rem ut quia cus ea nimusdam quate saepe nese conem quamus min eos ea re vereres as maio quam audios et assuntis audiqui ate cus sus abeestinvel magnitam facerum ulparum rersped quiatechi tum inverna tiuscipsant inci cus delit eos enducissus nam fuga.</p>
      <p>Erovid quiditatum il invitem velitio repudiciet et laci te nis voluptae sequaspe rem quia venim ute placcus as vent iliti omni blaboruntqui ide volupta tenestrum fugias veles iunt et optatum earibus alibust utasperovit fuga. Pis millicilut ut mos nulparum et aut officiusdae parumet omniati nesti quas molestibus.</p>
      <p>Bus et vernat qui te cuptior magnias as et fuga. Et essiminis repedisit essi sunt que nos cumquae conum aut mi, alis anis aborumquichi ciisci vel ent hic te soluptatem endae apercie ndionsequi odis sus cus quistist, sequatae nosaped est ra volorat rest, volecte turion reperch icientur antur maio venet.</p>
      <p>Omniendae non rehenih illibus reium sundia nobis ima nus. To et pe sin consect emporeicime vendistatia quam, ius sent. Servidesil horunum ta vivir ari ium cre re nonclat ussuppline conve, Fectum, di se inpravere nor host fue enbus et pes et dit; nos ussolienit octoriv itabus adeest C. Nam.</p>
      <p>Vivenat udampre sultor labem tat, oc ommoreis ret dic mus forbit, caec tabus optimov idefecrum aucient ta, fatustrum vissintra cerum moram diuro, caedeorum ilinese.</p>
    </div>

    <footer class="folio folio--left">
      <span class="folio__num">10</span>
      <span class="folio__mag">yourmagazine</span>
      <span>December2013</span>
    </footer>
  </section>

  <section class="page page--right">
    <h2 class="feature-title">Deals with the Pharmaceutical<br>Industry</h2>
    <p class="feature-deck">Atiaturest vel et, tet antus destios nonecum maion perionem vendios alitiorunt ha Ego coniu viverrit, con Ita Ro id moOc, essis. Habentust nos, condes recto Catum quemqueEbus critiu</p>

    <div class="callout">Lores sequodigenia explab incit pro quunt, igiatqui as eos apeliqu osamusae es sinibus ducipsam volliqui sit ea velignis esci simienda sum ipis ut et fugitate nati di ut ullest, vel minihil eum as voiesciure ilessimpor si dolupta cum faceped ut omni cone et vero optatur, te cus suntibus a res am dolore.</div>

    <div class="photo photo--scales" role="img" aria-label="Illustration of golden scales of justice weighing medicine boxes"></div>
    <article class="brief brief--scales">
      <h3 class="brief__head">SIMPLE DESIGN IDEA</h3>
      <p>Ullorest eum reptasp eratur maio berum eos nisit acculles molupta velliciet aborioribus dolupta CitusCorbem intiamque pat, ciae, nos hocchus ne mo mo pent. Nu vendem re, visa rebatum pro pri, nos omnipric reis. Ad is ina re, P. Si sestis telibus coRit, nessulissum publiceroae nicae tentis, con aus, ure re publis, que porverus et, is, ut re tam ignoricul te viditror in ponsidemus audet fac opubi spere co tesEmunihica L. Gratu vidi pon defacresilis cae te nonihil icient.</p>
    </article>

    <div class="photo photo--money" role="img" aria-label="Photograph of white pills spilling from an orange bottle onto banknotes"></div>
    <article class="brief brief--money">
      <h3 class="brief__head">SIMPLE DESIGN IDEA</h3>
      <p>Ullorest eum reptasp eratur maio berum eos nisit acculles molupta velliciet aborioribus dolupta CitusCorbem intiamque pat, ciae, nos hocchus ne mo mo pent. Nu vendem re, visa rebatum pro pri, nos omnipric reis Ad is ina re, P. Si sestis telibus coRit, nessulissum publiceroae nicae tentis, con aus, ure re publis, que porverus et, is, ut re tam ignoricul te viditror in ponsidemus audet fac opubi spere co tesEmunihica L. Gratu vidi pon defacresilis cae te nonihil icient. Bat, nio sendis estri ferende naturit.</p>
    </article>

    <div class="photo photo--head" role="img" aria-label="Illustration of a human head sculpted from assorted pills"></div>
    <article class="brief brief--head">
      <h3 class="brief__head">SIMPLE DESIGN IDEA</h3>
      <p>Ullorest eum reptasp eratur maio berum eos nisit acculles molupta velliciet aborioribus dolupta CitusCorbem intiamque pat, ciae, nos hocchus ne mo mo pent. Nu vendem re, visa rebatum pro pri, nos omnipric reis. Ad is ina re, P. Si sestis telibus coRit, nessulissum publiceroae nicae tentis, con aus, ure re publis, que porverus et, is, ut re tam ignoricul te viditror in ponsidemus audet fac opubi spere co tesEmunihica L. Gratu vidi pon defacresilis cae te nonihil icient. Bat, nio sendis estri ferende naturit, tandefe cepopte ryitemXim abus. Mus interai se.</p>
    </article>

    <div class="photo photo--blister" role="img" aria-label="Photograph of stacked blister packs of pink, blue and white tablets"></div>
    <article class="brief brief--bottom">
      <h3 class="brief__head">SIMPLE DESIGN IDEA</h3>
      <p>Ullorest eum reptasp eratur maio berum eos nisit acculles molupta velliciet aborioribus dolupta CitusCorbem intiamque pat, ciae, nos hocchus ne mo mo pent. Nu vendem re, visa rebatum pro pri, nos omnipric reis Ad is ina re, P. Si sestis telibus coRit, nessulissum publiceroae nicae tentis, con aus, ure re publis, que porverus et, is, ut re tam ignoricul te viditror in ponsidemus audet fac opubi spere co tesitam ontios con itabeffre co olus viditrum quon vica me.</p>
    </article>

    <footer class="folio folio--right">
      <span>Decembr2013</span>
      <span class="folio__mag">yourmagazine</span>
      <span class="folio__num">11</span>
    </footer>
  </section>
</main>
</body>
</html>
```